Neues Corporate Design für Steuerberaterin
Zielgruppe
Ich bin seit Kurzem als Steuerberaterin selbständig tätig. Meine Zielgruppe sind v.a. junge engagierte Leute zwischen 25 und 45 Jahren - Privatpersonen als auch Unternehmer - die ein bisschen anders denken und sich beim herkömmlichen Steuerberater nicht gut aufgehoben fühlen. Mir ist auch der persönliche/menschliche Aspekt mit meinen Kunden sehr wichtig (im Gegensatz zu vielen anderen), denn fachlich top sind eh die meisten und mein Eindruck ist, das alleine reicht nicht mehr aus.
Aufgabenstellung
Ich habe mich in den vergangenen Jahren bereits ein bisschen auf die Selbständigkeit vorbereitet und u.a. auch eine Visitenkarte entworfen (siehe Anhang). Allerdings ist das schon etwas länger her und ich finde diese 'alte' Visitenkarte nicht mehr ganz zeitgemäß bzw. auch zu undurchdacht. Das Logo (Weintraube und Paragraph) finde ich auch nicht mehr so passend (und etwas unseriös). Mir wär lieber ein schönen Schriftzug oder ein Logo mit Initialen oder sonst etwas Kreatives, damit das Ganze etwas professioneller wirkt. Meine Lieblingsfarbe ist violett, es kann aber auch gerne hell und dunkel gemischt werden. Ich könnte mir ebenfalls ein Farbspiel mit Kreisen oder Ecken oder sonst etwas vorstellen. Auf der Vorderseite der Visitenkarte hätte ich gerne 'Lena Brunner - Steuerberatung' stehen. Auf der Rückseite dann 'Steuerberaterin MMag. Lena Brunner' und alle Informationen die auch im Anhang zu finden sind. Ganz unten sollen graphisch abgegrenzt beiden Büro-Adressen stehen. So zumindest mal mein Vorschlag, bin aber auch für andere Ideen offen.

```html
<!DOCTYPE html>
<html lang="de">
<head>
<meta charset="utf-8">
<title>Lena Brunner – Steuerberatung</title>
<link rel="stylesheet" href="https://fonts.googleapis.com/css2?family=Arimo:wght@400;700&display=swap">
<style>
  :root {
    --violet: #861d5b;
    --paper: #ffffff;
    --stage: #e6e6e8;
    --ink: #111111;
    --card-shadow: rgba(40, 20, 40, 0.18);
  }
  * { margin: 0; padding: 0; box-sizing: border-box; }
  html, body { width: 1200px; height: 900px; overflow: hidden; }
  body {
    background: var(--stage);
    font-family: "Arimo", Arial, sans-serif;
    color: var(--violet);
    position: relative;
  }
  .card {
    position: absolute;
    width: 600px;
    height: 388px;
    background: var(--paper);
    box-shadow: 0 10px 30px var(--card-shadow);
    overflow: hidden;
  }
  .card-swoosh { position: absolute; inset: 0; width: 100%; height: 100%; }
  .card-front { left: 60px; top: 60px; }
  .card-back { left: 540px; top: 452px; }

  .wordmark {
    display: flex;
    align-items: center;
    gap: 14px;
    position: absolute;
  }
  .wordmark-square {
    width: 44px; height: 44px;
    background: var(--violet);
    flex: none;
  }
  .wordmark-text { display: flex; flex-direction: column; }
  .wordmark-name {
    font-weight: 700;
    font-size: 32px;
    letter-spacing: 1px;
    line-height: 1;
    white-space: nowrap;
    color: var(--violet);
  }
  .wordmark-tag {
    font-weight: 700;
    font-size: 11px;
    letter-spacing: 5px;
    margin-top: 6px;
    border-top: 1px solid var(--violet);
    padding-top: 4px;
    white-space: nowrap;
    color: var(--violet);
  }
  .card-front .wordmark { left: 170px; top: 205px; }
  .card-back .wordmark { left: 232px; top: 102px; }
  .card-back .wordmark-name { font-size: 26px; }
  .card-back .wordmark-square { width: 36px; height: 36px; }

  .holder-name {
    position: absolute;
    left: 30px; top: 182px;
    font-weight: 700;
    font-size: 25px;
    white-space: nowrap;
  }
  .contact-list {
    position: absolute;
    left: 318px; top: 222px;
    font-size: 12px;
    line-height: 1.45;
    white-space: nowrap;
  }
  .contact-list dt { font-weight: 700; display: inline; }
  .contact-list dd { display: inline; margin-left: 4px; }
  .contact-row { display: block; }

  .office-rule {
    position: absolute;
    left: 30px; right: 30px; top: 284px;
    border-top: 2px solid var(--violet);
  }
  .offices {
    position: absolute;
    left: 30px; top: 296px;
    display: flex;
    gap: 90px;
    font-size: 15px;
    line-height: 1.4;
  }
  .office { font-style: normal; }
  .office-title { font-weight: 700; }

  .brand-lockup {
    position: absolute;
    left: 760px; top: 180px;
    flex-direction: column;
    align-items: center;
    gap: 14px;
  }
  .brand-lockup .wordmark-square { width: 56px; height: 56px; background: var(--ink); }
  .brand-lockup .wordmark-name { color: var(--ink); font-size: 36px; }
  .brand-lockup .wordmark-tag { color: var(--ink); border-color: var(--ink); text-align: center; }
</style>
</head>
<body>

  <section class="card card-front" aria-label="Visitenkarte Vorderseite">
    <svg class="card-swoosh" viewBox="0 0 600 388" aria-hidden="true">
      <path d="M0,0 H600 V22 Q250,50 0,300 Z" fill="var(--violet)"/>
      <path d="M0,318 Q250,68 600,42" fill="none" stroke="var(--violet)" stroke-width="3"/>
    </svg>
    <div class="wordmark">
      <span class="wordmark-square"></span>
      <span class="wordmark-text">
        <span class="wordmark-name">LENA BRUNNER</span>
        <span class="wordmark-tag">STEUERBERATUNG</span>
      </span>
    </div>
  </section>

  <div class="wordmark brand-lockup">
    <span class="wordmark-square"></span>
    <span class="wordmark-text">
      <span class="wordmark-name">LENA BRUNNER</span>
      <span class="wordmark-tag">STEUERBERATUNG</span>
    </span>
  </div>

  <section class="card card-back" aria-label="Visitenkarte Rückseite">
    <svg class="card-swoosh" viewBox="0 0 600 388" aria-hidden="true">
      <path d="M0,0 H600 V14 Q240,28 0,170 Z" fill="var(--violet)"/>
      <path d="M0,186 Q240,44 600,30" fill="none" stroke="var(--violet)" stroke-width="3"/>
    </svg>
    <div class="wordmark">
      <span class="wordmark-square"></span>
      <span class="wordmark-text">
        <span class="wordmark-name">LENA BRUNNER</span>
        <span class="wordmark-tag">STEUERBERATUNG</span>
      </span>
    </div>
    <h1 class="holder-name">MMag. Lena Brunner, LL.M.</h1>
    <dl class="contact-list">
      <div class="contact-row"><dt>Mobil:</dt><dd>+43 660 18 32 705</dd></div>
      <div class="contact-row"><dt>E-Mail:</dt><dd>office@steuerberatung-brunner.at</dd></div>
      <div class="contact-row"><dt>Web:</dt><dd>www.steuerberatung-brunner.at</dd></div>
    </dl>
    <div class="office-rule"></div>
    <div class="offices">
      <address class="office">
        <span class="office-title">Büro Steiermark:</span><br>
        Lindenweg 12<br>8520 Grünau
      </address>
      <address class="office">
        <span class="office-title">Büro Wien:</span><br>
        Ahornplatz 4<br>1110 Wien
      </address>
    </div>
  </section>

</body>
</html>
```